Web Design Project for SEARCH ENGINE !

We need a website design for torrents search engine.

The Website will be www.Qorvexa.com

Qorvexa is a a search engine for torrents.
Qorvexa search and index torrents results from all torrents sites.

We will need:
Logo
WebSite Design
slogen (optional)

we need only PSDs - no codded pages are needed !

Design to the following screen Size & resolution: 1024 x 768

***PLEASE DOWNLOAD ATTACHED FILE !

```html
<!DOCTYPE html>
<html lang="en">
<head>
<meta charset="utf-8">
<title>Qorvexa – Torrent Meta-Search</title>
<link href="https://fonts.googleapis.com/css2?family=Open+Sans:ital,wght@0,400;0,600;0,700;1,700&display=swap" rel="stylesheet">
<style>
  :root {
    --navy-dark: #082f52;
    --navy: #0c4670;
    --navy-mid: #0f5486;
    --sky: #1aa3dc;
    --sky-deep: #1391c9;
    --sky-faint: rgba(255,255,255,0.10);
    --pill-ring: #0b4a78;
    --white: #ffffff;
    --ink: #1a1a1a;
    --link: #222222;
    --heading: #0d4a78;
    --footer-bg: #f1f1f1;
    --footer-ink: #0c3f6a;
    --badge-red: #d9483b;
  }
  * { box-sizing: border-box; margin: 0; padding: 0; }
  html, body { width: 1200px; height: 905px; overflow: hidden; }
  body { font-family: "Open Sans", sans-serif; color: var(--ink); background: var(--white); position: relative; }

  .site-header {
    position: absolute; left: 0; top: 0; width: 1200px; height: 88px;
    background: linear-gradient(180deg, var(--navy-mid) 0%, var(--navy-dark) 100%);
  }
  .brand { position: absolute; left: 47px; top: 12px; display: flex; align-items: center; gap: 12px; }
  .brand-mark { width: 62px; height: 62px; border-radius: 50%; background: var(--sky-deep); border: 3px solid #5fc3ee; }
  .brand-name { color: var(--white); font-weight: 700; font-size: 30px; letter-spacing: 0.5px; }
  .header-divider { position: absolute; left: 232px; top: 0; width: 2px; height: 88px; background: rgba(0,0,0,0.35); box-shadow: 1px 0 0 rgba(255,255,255,0.08); }
  .tagline { position: absolute; left: 255px; top: 26px; color: var(--white); font-size: 26px; font-weight: 700; font-style: italic; }

  .main-nav { position: absolute; right: 0; top: 0; height: 88px; display: flex; }
  .main-nav a {
    color: var(--white); text-decoration: none; font-weight: 700; font-size: 18px;
    line-height: 82px; padding: 0 18px;
    border-left: 2px solid rgba(0,0,0,0.3);
  }
  .main-nav a:first-child { border-left: none; }

  .hero {
    position: absolute; left: 0; top: 88px; width: 1200px; height: 330px;
    background: radial-gradient(ellipse at 50% 45%, #22aee6 0%, var(--sky) 50%, var(--sky-deep) 100%);
    border-top: 1px solid #5fc3ee;
  }
  .hero-icon { position: absolute; background: var(--sky-faint); border-radius: 4px; }
  .icon-music { left: 88px; top: 53px; width: 67px; height: 88px; }
  .icon-doc { left: 156px; top: 205px; width: 67px; height: 84px; }
  .icon-game { left: 926px; top: 32px; width: 64px; height: 85px; }
  .icon-movie { left: 1000px; top: 209px; width: 64px; height: 85px; }

  .search-form {
    position: absolute; left: 273px; top: 121px; width: 653px; height: 80px;
    border-radius: 40px; background: var(--pill-ring);
    box-shadow: 0 14px 18px rgba(0,60,100,0.25);
  }
  .search-input {
    position: absolute; left: 8px; top: 8px; width: 637px; height: 64px; border-radius: 32px;
    background: linear-gradient(180deg, #ffffff 0%, #eeeeee 100%);
    font-size: 18px; color: #333; line-height: 64px; padding-left: 38px;
  }
  .search-button {
    position: absolute; right: 20px; top: 14px; width: 52px; height: 52px; border-radius: 50%;
    background: radial-gradient(circle at 40% 35%, #4aa8e0 0%, #0d4f88 80%);
    border: 2px solid #ffffff;
  }

  .info-band {
    position: absolute; left: 0; top: 418px; width: 1200px; height: 82px;
    background: linear-gradient(180deg, var(--navy) 0%, #0a3d64 100%);
  }
  .info-text { position: absolute; left: 66px; top: 13px; color: var(--white); font-size: 19.5px; line-height: 27px; }
  .info-text strong { font-style: italic; font-size: 25px; }
  .share-badge { position: absolute; left: 963px; top: 27px; width: 51px; height: 35px; border-radius: 4px; background: #f3f3f3; border-top: 4px solid var(--badge-red); }
  .share-count {
    position: absolute; left: 1029px; top: 29px; width: 83px; height: 34px; border-radius: 4px;
    background: var(--white); color: var(--navy); font-weight: 700; font-size: 15px; text-align: center; line-height: 34px;
  }
  .share-count::before {
    content: ""; position: absolute; left: -7px; top: 11px;
    border-style: solid; border-width: 6px 7px 6px 0; border-color: transparent var(--white) transparent transparent;
  }

  .content-fade { position: absolute; left: 0; top: 500px; width: 1200px; height: 50px; background: linear-gradient(180deg, #eeeeee 0%, #ffffff 100%); }
  .index-stats { position: absolute; left: 0; top: 559px; width: 1200px; text-align: center; font-size: 17.5px; }
  .stats-rule { position: absolute; left: 295px; top: 599px; width: 611px; border-top: 1px dashed #888; }
  .categories-title { position: absolute; left: 0; top: 608px; width: 1200px; text-align: center; color: var(--heading); font-size: 28px; font-weight: 700; font-style: italic; }
  .category-links { position: absolute; left: 0; top: 646px; width: 1200px; text-align: center; font-size: 18px; color: var(--link); }
  .category-links a { color: var(--link); text-decoration: underline; }
  .category-links .sep { margin: 0 7px; }

  .site-footer {
    position: absolute; left: 0; top: 854px; width: 1200px; height: 51px; background: var(--footer-bg);
    color: var(--footer-ink); font-weight: 700; font-size: 15px; line-height: 51px;
  }
  .footer-copy { position: absolute; left: 38px; }
  .footer-links { position: absolute; right: 37px; }
  .footer-links a { color: var(--footer-ink); text-decoration: none; }
  .footer-links .sep { margin: 0 6px; }
</style>
</head>
<body>
  <header class="site-header">
    <div class="brand">
      <span class="brand-mark"></span>
      <span class="brand-name">Qorvexa</span>
    </div>
    <span class="header-divider"></span>
    <p class="tagline">Download all what you want...</p>
    <nav class="main-nav">
      <a href="#">Search</a>
      <a href="#">Qorvexa</a>
      <a href="#">Profile</a>
      <a href="#">Help</a>
    </nav>
  </header>

  <section class="hero">
    <div class="hero-icon icon-music" role="img" aria-label="Faint music file icon"></div>
    <div class="hero-icon icon-doc" role="img" aria-label="Faint e-book file icon"></div>
    <div class="hero-icon icon-game" role="img" aria-label="Faint game file icon"></div>
    <div class="hero-icon icon-movie" role="img" aria-label="Faint movie file icon"></div>
    <form class="search-form">
      <div class="search-input">Search Torrent...</div>
      <span class="search-button" role="img" aria-label="Search button"></span>
    </form>
  </section>

  <section class="info-band">
    <p class="info-text"><strong>Qorvexa</strong> is a free, fast &amp; powerful meta-search engine combining results from<br>dozens of torrent search engines</p>
    <span class="share-badge" role="img" aria-label="Share badge"></span>
    <span class="share-count">37.3 K</span>
  </section>

  <div class="content-fade"></div>
  <p class="index-stats">Indexing 15, 337, 488 active torrents from 60, 307, 316 pages on 33 domains</p>
  <hr class="stats-rule">
  <h2 class="categories-title">Popular Categories:</h2>
  <p class="category-links">
    <a href="#">Games </a><span class="sep">|</span><a href="#">Movies</a><span class="sep">|</span><a href="#">E-Books</a><span class="sep">|</span><a href="#">Songs</a><span class="sep">|</span><a href="#">Softwares</a>
  </p>

  <footer class="site-footer">
    <span class="footer-copy">Copyright 2011 Qorvexa &nbsp;|&nbsp; All Rights Reserved</span>
    <span class="footer-links"><a href="#">Privacy Policy</a><span class="sep">|</span><a href="#">Legal</a><span class="sep">|</span><a href="#">Contact Us</a></span>
  </footer>
</body>
</html>
```